Graphic of Teacher Agility Framework

I need a model designed for my teacher educator agility framework. The concepts are responsive to each other on Figure 12 on the attachment and the text explains it all.

This is meant to be a conceptual framework of how ones thinks between experience, and theory, and research.

The domains represent a hierarchy of knowledge of specific domains that have enabled my learning to develop in-depth. I chose the term ‘agility framework’ to emphasise the importance of a responsiveness to the context and of the ability to respond with urgency between the various components (The Corvane Digest, 2012). I present the agility framework in Figure 12. The concentric circles are inter-connected as they are inter-dependent aspects of developing personal empowerment. The applicability of each domain relies on my ability to be aware of the context and to build work with urgency.

My learning has been iterative throughout this research, so this framework is intended to be understood as iterative, with movement between the concentric circles at a cognitive and behavioural level when greater awareness is gained. At the heart of the main circle are the researcherly dispositions that have been essential to my research and professional roles as well as to my personal learning. I have used descriptive headings for these dispositions that I believe are helpful for understanding them. The first one, ‘value deep understanding’, is modelled on Dortvelt (2019); whilst ‘cognitive flexibility’ is an inter-cultural competency from Lasko et al (2014). I have also added in ‘responsiveness’ and ‘sensory awareness’ which I believe are additional dispositions that have emerged in this study. Whilst conducting this research I have been responsive to the context, the participants, and the data, whilst gaining a greater awareness of my place within UAE society.

Target Market(s)

Academic, research

Requirements
Must have
• Attractive Visuals
Nice to have
• Connections between the concepts

```html
<!DOCTYPE html>
<html lang="en">
<head>
<meta charset="utf-8">
<title>Teacher Educator Agility Framework</title>
<link rel="stylesheet" href="https://fonts.googleapis.com/css2?family=Roboto:wght@500;700&display=swap">
<style>
  :root {
    --bg: #ffffff;
    --ink: #1a1a1a;
    --line: #333333;
    --blue: #0070ba;
    --gold: #ffc20e;
    --amber: #e8a600;
    --purple: #8b55a0;
    --red: #e04848;
    --agency: #ffd35c;
    --tensions: #e9868f;
    --tacit: #5aa3d8;
    --power: #a98bc7;
    --dot: #1467b0;
  }
  html, body {
    margin: 0;
    width: 1200px;
    height: 1200px;
    overflow: hidden;
    background: var(--bg);
  }
  .framework {
    display: block;
    width: 1200px;
    height: 1200px;
    font-family: "Roboto", Arial, sans-serif;
  }
  .label-white { fill: #fff; font-weight: 700; }
  .label-dark { fill: var(--ink); font-weight: 700; }
  .ring-title { font-size: 15px; }
  .disposition { font-size: 11px; }
  .checklist-item { font-size: 11px; }
  .factor-label { font-size: 11px; }
  .venn-label { font-size: 11px; }
  .venn-circle { stroke: var(--line); stroke-width: 2; mix-blend-mode: multiply; opacity: .9; }
</style>
</head>
<body>
<svg class="framework" viewBox="0 0 1080 1080" role="img" aria-label="Teacher educator agility framework: concentric circles of dispositions, consumption of research, context and relationships, and inter-cultural competence, linked to external factors and personal empowerment">
  <defs>
    <path id="research-arc" d="M452,507 A128,128 0 0 1 708,507"/>
    <path id="competence-arc" d="M318,507 A262,262 0 0 0 842,507"/>
  </defs>

  <!-- outer timeline arc with factors -->
  <g class="factor-arc">
    <path d="M581,197 A310,310 0 0 1 581,817" fill="none" stroke="var(--line)" stroke-width="1.5"/>
    <g fill="var(--dot)" stroke="var(--line)" stroke-width="1.2">
      <circle cx="581" cy="197" r="6"/>
      <circle cx="581" cy="817" r="6"/>
      <circle cx="874" cy="409" r="6"/>
      <circle cx="886" cy="457" r="6"/>
      <circle cx="890" cy="506" r="6"/>
      <circle cx="886" cy="555" r="6"/>
      <circle cx="874" cy="604" r="6"/>
    </g>
    <text class="label-dark factor-label" x="900" y="413">Time</text>
    <text class="label-dark factor-label" x="910" y="461">Speed</text>
    <text class="label-dark factor-label" x="915" y="510">Urgency</text>
    <text class="label-dark factor-label" x="904" y="559">Awareness of self</text>
    <text class="label-dark factor-label" x="896" y="608">Reflexivity</text>
  </g>

  <!-- inter-cultural competence ring -->
  <circle cx="580" cy="507" r="295" fill="var(--blue)"/>
  <circle cx="580" cy="507" r="240" fill="var(--bg)" stroke="var(--line)" stroke-width="1.5"/>
  <circle cx="580" cy="507" r="225" fill="var(--bg)" stroke="var(--line)" stroke-width="1.5"/>
  <text class="label-white ring-title"><textPath href="#competence-arc" startOffset="50%" text-anchor="middle">Inter-cultural competence</textPath></text>

  <!-- context / relationships cycle -->
  <g class="cycle">
    <path d="M770,507 A190,190 0 0 1 390,507" fill="none" stroke="var(--amber)" stroke-width="52"/>
    <polygon points="338,507 428,507 383,462" fill="var(--amber)" stroke="var(--bg)" stroke-width="3"/>
    <path d="M390,507 A190,190 0 0 1 770,507" fill="none" stroke="var(--gold)" stroke-width="52"/>
    <polygon points="732,505 822,505 777,550" fill="var(--gold)" stroke="var(--bg)" stroke-width="3"/>
    <text class="label-white ring-title" x="585" y="317" text-anchor="middle">Context</text>
    <text class="label-white ring-title" x="580" y="706" text-anchor="middle">Relationships</text>
  </g>

  <!-- consumption of research -->
  <circle cx="580" cy="507" r="163" fill="var(--purple)" stroke="var(--line)" stroke-width="1.5"/>
  <text class="label-white ring-title"><textPath href="#research-arc" startOffset="50%" text-anchor="middle">Consumption of Research</textPath></text>
  <circle cx="580" cy="507" r="117" fill="var(--bg)" stroke="var(--line)" stroke-width="1.5"/>

  <!-- researcherly dispositions -->
  <g class="dispositions">
    <circle cx="580" cy="507" r="104" fill="var(--red)"/>
    <line x1="580" y1="403" x2="580" y2="611" stroke="var(--bg)" stroke-width="2"/>
    <line x1="476" y1="507" x2="684" y2="507" stroke="var(--bg)" stroke-width="2"/>
    <text class="label-white disposition" text-anchor="middle"><tspan x="540" y="462">Sensory</tspan><tspan x="540" y="476">Awareness</tspan></text>
    <text class="label-white disposition" text-anchor="middle"><tspan x="622" y="465">Value Deep</tspan><tspan x="631" y="479">Understanding</tspan></text>
    <text class="label-white disposition" x="533" y="551" text-anchor="middle">Responsiveness</text>
    <text class="label-white disposition" text-anchor="middle"><tspan x="618" y="551">Cognitive</tspan><tspan x="618" y="565">Flexibility</tspan></text>
  </g>

  <!-- connecting double arrows -->
  <g class="connector" fill="var(--gold)" stroke="var(--line)" stroke-width="1.5" stroke-linejoin="round">
    <polygon points="280,352 310,327 310,342 440,342 440,327 470,352 440,378 440,362 310,362 310,378"/>
    <polygon points="280,667 310,642 310,657 440,657 440,642 470,667 440,693 440,677 310,677 310,693"/>
  </g>
  <g stroke="var(--bg)" stroke-width="3">
    <line x1="310" y1="347" x2="440" y2="347"/>
    <line x1="310" y1="662" x2="440" y2="662"/>
  </g>

  <!-- external factors box -->
  <g class="external-factors">
    <rect x="69" y="246" width="200" height="147" rx="18" fill="var(--bg)" stroke="var(--line)" stroke-width="1.5"/>
    <rect x="72" y="252" width="190" height="138" rx="15" fill="var(--gold)"/>
    <g fill="none" stroke="#fff" stroke-width="1.4">
      <circle cx="95" cy="295" r="5"/><path d="M92,295 l2.5,2.5 l5,-6"/>
      <circle cx="95" cy="314" r="5"/><path d="M92,314 l2.5,2.5 l5,-6"/>
      <circle cx="95" cy="332" r="5"/><path d="M92,332 l2.5,2.5 l5,-6"/>
      <circle cx="95" cy="352" r="5"/><path d="M92,352 l2.5,2.5 l5,-6"/>
    </g>
    <text class="label-white checklist-item" x="112" y="299">Employment Contracts</text>
    <text class="label-white checklist-item" x="112" y="319">Cultural Differences</text>
    <text class="label-white checklist-item" x="112" y="337">Education Regulations</text>
    <text class="label-white checklist-item" x="112" y="357">Macro Economic Factors</text>
  </g>

  <!-- personal empowerment -->
  <g class="empowerment">
    <text class="label-dark factor-label" text-anchor="middle"><tspan x="172" y="468">Personal</tspan><tspan x="172" y="482">Empowerment</tspan></text>
    <line x1="172" y1="571" x2="172" y2="500" stroke="var(--line)" stroke-width="2"/>
    <path d="M161,512 L172,500 L183,512" fill="none" stroke="var(--line)" stroke-width="2"/>
  </g>

  <g class="venn">
    <circle class="venn-circle" cx="135" cy="631" r="59" fill="var(--agency)"/>
    <circle class="venn-circle" cx="208" cy="631" r="59" fill="var(--tensions)"/>
    <circle class="venn-circle" cx="135" cy="708" r="59" fill="var(--tacit)"/>
    <circle class="venn-circle" cx="208" cy="708" r="59" fill="var(--power)"/>
    <text class="label-white venn-label" x="118" y="634" text-anchor="middle">Agency</text>
    <text class="label-white venn-label" x="227" y="634" text-anchor="middle">Tensions</text>
    <text class="label-white venn-label" text-anchor="middle"><tspan x="124" y="709">Tacit</tspan><tspan x="113" y="723">Knowledge</tspan></text>
    <text class="label-white venn-label" text-anchor="middle"><tspan x="221" y="712">Power</tspan><tspan x="221" y="726">Grow</tspan></text>
  </g>
</svg>
</body>
</html>
```